We need visit card and a letter paper for our website. thx

We have a beauty clinic in Switzerland.
https://wolkenbachtal.ch
We need a visit card.

Requirements
Must have
• see colors on website

```html
<!DOCTYPE html>
<html lang="en">
<head>
<meta charset="utf-8">
<title>Wolkenbachtal – Business Cards</title>
<link href="https://fonts.googleapis.com/css2?family=Lato:wght@400;700&family=Arimo:wght@400;700&family=Oswald:wght@400&display=swap" rel="stylesheet">
<style>
  :root {
    --backdrop: #7d7d7d;
    --card: #3b3b3b;
    --ink: #f2f2f2;
    --rule: #8a8a8a;
    --photo-light: #9a9a9a;
    --photo-dark: #2a2a2a;
  }
  html, body {
    margin: 0; padding: 0;
    width: 1200px; height: 1200px;
    overflow: hidden;
    background: var(--backdrop);
  }
  .canvas { position: relative; width: 1200px; height: 1200px; }
  .card {
    position: absolute;
    top: 310px;
    height: 595px;
    background: var(--card);
    color: var(--ink);
    text-align: center;
    font-family: "Arimo", Arial, sans-serif;
  }
  .card--lena { left: 234px; width: 365px; }
  .card--felix { left: 627px; width: 370px; }
  .card > * { position: absolute; left: 0; right: 0; margin: 0; }
  .portrait {
    left: 50%;
    width: 158px; height: 158px;
    transform: translateX(-50%);
    right: auto;
  }
  .portrait--lena { top: 67px; background: linear-gradient(160deg, var(--photo-light), var(--photo-dark)); }
  .portrait--felix { top: 52px; background: radial-gradient(circle at 50% 45%, var(--photo-light), var(--photo-dark) 75%); }
  .name { font-family: "Lato", sans-serif; font-weight: 700; }
  .name--lena { top: 238px; font-size: 24px; }
  .name--felix { top: 229px; font-size: 20px; }
  .name .title { font-weight: 400; }
  .hotline-label { top: 320px; font-weight: 700; font-size: 19px; }
  .hotline-number { top: 347px; font-family: "Oswald", sans-serif; font-size: 24px; }
  .rule { height: 1px; background: var(--rule); left: 50%; right: auto; transform: translateX(-50%); }
  .rule--w150 { width: 150px; }
  .contact { font-size: 16.5px; line-height: 30px; }
  .contact--lena { top: 406px; }
  .contact--felix { top: 290px; line-height: 22px; }
  .address { font-size: 16.5px; line-height: 22px; }
  .address--lena { top: 501px; }
  .address--felix { top: 381px; }
  .brand-name {
    top: 486px;
    font-family: "Lato", sans-serif;
    font-weight: 400;
    font-size: 36px;
  }
</style>
</head>
<body>
<main class="canvas">
  <section class="card card--lena">
    <div class="portrait portrait--lena" role="img" aria-label="Portrait photo of Dr. Lena Marbach"></div>
    <h2 class="name name--lena">Dr. Lena Marbach</h2>
    <p class="hotline-label">Free 24-hour beauty hotline</p>
    <p class="hotline-number">+41 (0) 800 22 40 40</p>
    <div class="rule rule--w150" style="top:394px"></div>
    <p class="contact contact--lena">hallo@wolkenbachtal.ch<br>www.wolkenbachtal.ch</p>
    <div class="rule rule--w150" style="top:478px"></div>
    <p class="address address--lena">Talweg 14, 7550 Bergdorf<br>Switzerland</p>
  </section>

  <section class="card card--felix">
    <div class="portrait portrait--felix" role="img" aria-label="Portrait photo of Dr. Felix Aeberli"></div>
    <h2 class="name name--felix">Dr. Felix Aeberli, <span class="title">DESA</span></h2>
    <div class="rule rule--w150" style="top:280px"></div>
    <p class="contact contact--felix">+41 (0) 800 22 40 40<br>hallo@wolkenbachtal.ch<br>www.wolkenbachtal.ch</p>
    <div class="rule rule--w150" style="top:367px"></div>
    <p class="address address--felix">Talweg 14, 7550 Bergdorf<br>Switzerland</p>
    <p class="brand-name">Wolkenbachtal</p>
  </section>
</main>
</body>
</html>
```